| ■お仕事内容 海外の高級ファッションブランドを販売するサイト用の無償修理保証のバナー製作をお願いいたします。 メンズ、レディースどちらも取り扱っているブランドのため、どちらでも使えるデザインが望ましいです。 ■バナーに記載する内容 「1年間無償修理保証」ということが伝わる文章を入れてください。 ※独自のサービスのため、「当店だけの・・・」など独自の付加価値サービスである文言を入れたいです。 ■重視する点 ・高級感のあるデザイン(ごちゃごちゃしていない、シンプルで目を引くもの) ・フラットデザインが基調になっているサイトにマッチするデザイン ・ファッション系のサイトに合うデザイン ・本物である安心感・信頼感のあるデザイン ■報酬 5,000円 ■応募条件 WEBサイトのバナー、アイコンなどの製作経験をお持ちの方 ご提案価格と実績のバランスを見てお仕事をお願いする方を選定させていただきます。 たくさんのご応募お待ちしております。 何卒宜しくお願いいたします。 |

```html
<!DOCTYPE html>
<html lang="ja">
<head>
<meta charset="UTF-8">
<title>1年間無償修理保証</title>
<link href="https://fonts.googleapis.com/css2?family=Great+Vibes&family=Noto+Sans+JP:wght@500;700&family=Noto+Serif+JP:wght@500;600&display=swap" rel="stylesheet">
<style>
  :root {
    --ink: #0b0b0b;
    --gold: #a58f55;
    --gold-deep: #8a7542;
    --gold-text: #cdb57c;
    --white: #ffffff;
  }
  html, body {
    margin: 0;
    padding: 0;
    width: 1200px;
    height: 262px;
    overflow: hidden;
    background: var(--ink);
  }
  .banner {
    position: relative;
    width: 1200px;
    height: 262px;
    background: var(--ink);
    overflow: hidden;
  }
  .badge {
    position: absolute;
    left: 0;
    top: 0;
  }
  .badge-script {
    position: absolute;
    left: 14px;
    top: 48px;
    width: 350px;
    transform: rotate(-14deg);
    transform-origin: center;
    font-family: "Great Vibes", cursive;
    color: var(--white);
    font-size: 72px;
    line-height: 0.95;
    letter-spacing: 1px;
  }
  .badge-script .line-two {
    display: block;
    padding-left: 30px;
  }
  .copy {
    position: absolute;
    left: 410px;
    top: 22px;
    right: 30px;
  }
  .lead {
    margin: 0;
    font-family: "Noto Sans JP", sans-serif;
    font-weight: 700;
    font-size: 40px;
    color: var(--white);
    letter-spacing: 1px;
    line-height: 1.2;
  }
  .headline {
    margin: 32px 0 0 0;
    font-family: "Noto Serif JP", serif;
    font-weight: 500;
    font-size: 78px;
    color: var(--gold-text);
    letter-spacing: 4px;
    line-height: 1.1;
    white-space: nowrap;
  }
</style>
</head>
<body>
  <div class="banner">
    <svg class="badge" width="400" height="262" viewBox="0 0 400 262" aria-hidden="true">
      <defs>
        <linearGradient id="goldFill" x1="0" y1="0" x2="1" y2="1">
          <stop offset="0" stop-color="#b29c60"/>
          <stop offset="1" stop-color="#8a7542"/>
        </linearGradient>
      </defs>
      <circle cx="-100" cy="131" r="480" fill="url(#goldFill)"/>
    </svg>
    <div class="badge-script">Special<span class="line-two">Service!</span></div>
    <div class="copy">
      <p class="lead">当店だけの“スペシャルサービス”</p>
      <p class="headline">1年間無償修理保証</p>
    </div>
  </div>
</body>
</html>
```